Health Coaching Flyer for New Clients

I need a two-sided flyer (3.5" x 8.5" preferred or 5" x 7") to distribute to potential coaching clients. My business name is Talvery Health & Wellness Coaching. My business is focused on helping people with habit changes that contribute to their overall well-being. I would like the design colors to be gender neutral. I would like a small photo of myself near the "my name is Joan" statement. Please feel free to change the logo color to match the design.

Target Market(s)

Adults of all ages.

Font styles to use
Serif

Requirements
Must have
• Emphasize my opening question (found in health coaching brochure - attached).
• Small picture of myself near "my name is Joan" statement.
Should not have
• No light of pastel colors.

```html
<!DOCTYPE html>
<html lang="en">
<head>
<meta charset="utf-8">
<title>Talvery Health &amp; Wellness Coaching – Rack Card</title>
<link href="https://fonts.googleapis.com/css2?family=Montserrat:ital,wght@0,700;0,800;1,800;1,900&family=Roboto:ital,wght@0,400;0,500;1,400;1,500&display=swap" rel="stylesheet">
<style>
  :root{
    --bg:#b8bbbf;
    --ink:#1e1f21;
    --dark:#262728;
    --dark-2:#3b3c3e;
    --blue:#0ea0e8;
    --blue-deep:#2d7fdc;
    --white:#ffffff;
    --muted:#e6e6e6;
  }
  *{box-sizing:border-box;margin:0;padding:0}
  html,body{width:1200px;height:1200px;overflow:hidden;background:var(--bg)}
  .canvas{position:relative;width:1200px;height:1200px;background:var(--bg)}
  .card{position:absolute;width:415px;height:1008px;overflow:hidden;
        background:linear-gradient(180deg,var(--dark) 0%,#343537 60%,var(--dark) 100%);
        box-shadow:0 8px 22px rgba(0,0,0,.35);color:var(--white);
        font-family:"Roboto",Arial,sans-serif}
  .card--front{left:153px;top:62px}
  .card--back{left:634px;top:60px}
  .abs{position:absolute}

  .masthead{position:absolute;left:0;top:0;width:100%;height:100px;display:flex;align-items:center;gap:12px;padding-left:38px}
  .card--front .masthead{background:#000}
  .card--back .masthead{background:var(--blue-deep)}
  .brand-mark{width:14px;height:14px;background:var(--white)}
  .brand-name{font-family:"Montserrat",Arial,sans-serif;font-weight:800;color:var(--white);line-height:1.05}
  .brand-name .big{display:block;font-size:42px;letter-spacing:2px}
  .brand-name .small{display:block;font-size:13px;letter-spacing:.2px}

  .hero-photo{left:0;top:100px;width:415px;height:300px}
  .hero-wave{left:0;top:300px;width:415px;height:110px}

  .headline{left:0;top:497px;width:100%;text-align:center;font-family:"Montserrat",Arial,sans-serif;font-style:italic;font-weight:900;line-height:1}
  .headline .l1{font-size:37px;display:block}
  .headline .l2{font-size:22.5px;display:block;margin-top:3px}
  .headline .l3{font-size:24px;display:block;color:var(--blue);margin-top:2px}
  .headline .l4{font-size:37px;display:block;color:var(--blue);margin-top:1px}
  .rule{height:2px;background:#8a8b8d}
  .intro{left:38px;top:642px;width:340px;text-align:center;font-style:italic;font-size:16.4px;line-height:20.8px;color:var(--muted)}

  .contact-band{left:0;top:836px;width:100%;height:172px;background:var(--blue)}
  .portrait{left:-8px;top:822px;width:168px;height:190px;border-radius:0 95px 95px 0;background:linear-gradient(160deg,#4a3a30,#8b6e5e 60%,#2b2522);border-right:6px solid var(--dark)}
  .pill{background:var(--white);color:var(--ink);border-radius:20px;font-family:"Montserrat",Arial,sans-serif;font-style:italic;font-weight:900;text-align:center;box-shadow:0 2px 4px rgba(0,0,0,.3)}
  .contact-pill{left:120px;top:861px;width:278px;height:36px;line-height:36px;font-size:19px}
  .contact-text{left:198px;top:910px;width:212px;font-size:14.5px;line-height:18.5px}
  .contact-text .note{font-style:italic;display:block;margin-bottom:2px}
  .contact-text .who{font-weight:500;font-size:16px;display:block}
  .contact-text .row{display:flex;align-items:center;gap:6px}
  .contact-text svg{width:13px;height:13px;flex:none}

  .back-title{left:0;top:120px;width:100%;text-align:center;font-family:"Montserrat",Arial,sans-serif;font-style:italic;font-weight:900;font-size:30px;line-height:29px}
  .benefits{left:30px;top:195px;width:360px;list-style:none}
  .benefits li{display:flex;gap:18px;font-size:17.6px;line-height:21.8px;margin-bottom:8px}
  .benefits svg{width:32px;height:34px;flex:none;margin-top:2px}

  .offer-bg{left:0;top:525px;width:415px;height:483px}
  .offer-copy{left:28px;width:360px;text-align:center;color:var(--ink);font-size:17px;line-height:21.8px}
  .offer-pill{left:37px;top:768px;width:342px;height:32px;line-height:32px;background:var(--ink);color:var(--white);font-size:18px}
  .offer-note{left:0;top:814px;width:100%;text-align:center;color:var(--ink);font-style:italic;font-weight:500;font-size:14px}
  .card--back .contact-band{background:var(--dark-2);top:850px}
  .card--back .portrait{top:820px;border-right-color:var(--blue)}
  .card--back .contact-pill{top:858px}
  .card--back .contact-text{top:907px}
</style>
</head>
<body>
<div class="canvas">

  <section class="card card--front">
    <header class="masthead">
      <span class="brand-mark"></span>
      <div class="brand-name"><span class="big">TALVERY</span><span class="small">HEALTH &amp; WELLNESS COACHING</span></div>
    </header>

    <div class="abs hero-photo" role="img" aria-label="Photo of a man and a woman jogging together beside a lake at sunrise"
         style="background:linear-gradient(180deg,#9fb8cc 0%,#dfe6ea 35%,#8aa6ba 60%,#4f6f86 100%)"></div>
    <svg class="abs hero-wave" viewBox="0 0 415 110" preserveAspectRatio="none">
      <path d="M0 10 C90 90 250 90 415 0 L415 110 L0 110 Z" fill="#0b5fb8"/>
      <path d="M0 40 C100 105 260 100 415 45 L415 110 L0 110 Z" fill="#0ea0e8"/>
      <path d="M0 62 C110 118 270 112 415 70 L415 110 L0 110 Z" fill="#262728"/>
    </svg>

    <h1 class="abs headline">
      <span class="l1">NEED SUPPORT</span>
      <span class="l2">IN MAKING REAL LASTING</span>
      <span class="l3">LIFESTYLE &amp; BEHAVIOR</span>
      <span class="l4">CHANGES?</span>
    </h1>
    <div class="abs rule" style="left:95px;top:628px;width:240px"></div>

    <p class="abs intro">My name is Joan.&nbsp; I am studying to become an VERANT-Certified Functional HealtCoach. My training involves many science-based practices that improve both our health and how we grow and change as humans. I now have the opportunity to turn that knowledge into practice by coaching actual clients interested in improving their own health and well-being.</p>

    <div class="abs contact-band"></div>
    <div class="abs portrait" role="img" aria-label="Portrait photo of Joan Talvery"></div>
    <div class="abs pill contact-pill">PLEASE CONTACT ME</div>
    <div class="abs contact-text">
      <span class="note">I’m ready to support you as you work to improve your health.</span>
      <span class="who">Joan Talvery</span>
      <span class="row"><svg viewBox="0 0 24 24"><path d="M6.6 10.8a15 15 0 0 0 6.6 6.6l2.2-2.2c.3-.3.7-.4 1-.2 1.1.4 2.3.6 3.6.6.6 0 1 .4 1 1V20c0 .6-.4 1-1 1A17 17 0 0 1 3 4c0-.6.4-1 1-1h3.5c.6 0 1 .4 1 1 0 1.3.2 2.5.6 3.6.1.3 0 .7-.2 1z" fill="#fff"/></svg>555-014-2298</span>
      <span class="row"><svg viewBox="0 0 24 24"><rect x="3" y="5" width="18" height="14" fill="none" stroke="#fff" stroke-width="2"/><path d="M3 6l9 7 9-7" fill="none" stroke="#fff" stroke-width="2"/></svg>talveryhwc@example.com</span>
    </div>
  </section>

  <section class="card card--back">
    <header class="masthead">
      <span class="brand-mark"></span>
      <div class="brand-name"><span class="big">TALVERY</span><span class="small">HEALTH &amp; WELLNESS COACHING</span></div>
    </header>

    <h2 class="abs back-title">FUNCTIONAL<br>HEALTH COACHES</h2>
    <div class="abs rule" style="left:108px;top:182px;width:240px;background:#bdbdbd"></div>

    <ul class="abs benefits">
      <li><svg viewBox="0 0 32 34"><rect x="2" y="8" width="24" height="24" fill="none" stroke="#2d7fdc" stroke-width="2.5"/><path d="M7 19l6 7L30 2" fill="none" stroke="#2d7fdc" stroke-width="4"/></svg><span>Leverage your strengths rather than focus on your weaknesses</span></li>
      <li><svg viewBox="0 0 32 34"><rect x="2" y="8" width="24" height="24" fill="none" stroke="#2d7fdc" stroke-width="2.5"/><path d="M7 19l6 7L30 2" fill="none" stroke="#2d7fdc" stroke-width="4"/></svg><span>Support you in finding your own strategies and motivation for change</span></li>
      <li><svg viewBox="0 0 32 34"><rect x="2" y="8" width="24" height="24" fill="none" stroke="#2d7fdc" stroke-width="2.5"/><path d="M7 19l6 7L30 2" fill="none" stroke="#2d7fdc" stroke-width="4"/></svg><span>Provide a judgment-free zone and support your autonomy</span></li>
      <li><svg viewBox="0 0 32 34"><rect x="2" y="8" width="24" height="24" fill="none" stroke="#2d7fdc" stroke-width="2.5"/><path d="M7 19l6 7L30 2" fill="none" stroke="#2d7fdc" stroke-width="4"/></svg><span>Use an experimental mindset to find and develop sustainable habits</span></li>
      <li><svg viewBox="0 0 32 34"><rect x="2" y="8" width="24" height="24" fill="none" stroke="#2d7fdc" stroke-width="2.5"/><path d="M7 19l6 7L30 2" fill="none" stroke="#2d7fdc" stroke-width="4"/></svg><span>Act as your accountability partner as you reach your unique health goals; whether they be improving sleep, diet, fitness, social connection, or reducing stress.</span></li>
    </ul>

    <svg class="abs offer-bg" viewBox="0 0 415 483" preserveAspectRatio="none">
      <path d="M0 40 Q207 -40 415 40 L415 483 L0 483 Z" fill="#fff"/>
      <path d="M0 46 Q207 -30 415 46 L415 483 L0 483 Z" fill="#0ea0e8"/>
    </svg>

    <svg class="abs" style="left:183px;top:546px" width="66" height="62" viewBox="0 0 66 62">
      <rect x="3" y="8" width="54" height="46" rx="4" fill="#fff"/>
      <rect x="14" y="3" width="5" height="10" rx="2" fill="#fff" stroke="#0ea0e8" stroke-width="1.5"/>
      <rect x="41" y="3" width="5" height="10" rx="2" fill="#fff" stroke="#0ea0e8" stroke-width="1.5"/>
      <line x1="3" y1="21" x2="57" y2="21" stroke="#0ea0e8" stroke-width="2"/>
      <g fill="#0ea0e8"><rect x="10" y="26" width="6" height="5"/><rect x="20" y="26" width="6" height="5"/><rect x="30" y="26" width="6" height="5"/><rect x="40" y="26" width="6" height="5"/><rect x="10" y="35" width="6" height="5"/><rect x="20" y="35" width="6" height="5"/><rect x="30" y="35" width="6" height="5"/><rect x="10" y="44" width="6" height="5"/><rect x="20" y="44" width="6" height="5"/></g>
      <circle cx="53" cy="49" r="11" fill="#fff" stroke="#0ea0e8" stroke-width="2"/>
      <path d="M48 49l4 4 7-8" fill="none" stroke="#0ea0e8" stroke-width="2.5"/>
    </svg>

    <p class="abs offer-copy" style="top:613px">I would like to invite you to participate with me as a client as I continue to hone my coaching skills.&nbsp; We can develop a plan and schedule that aligns with your goals.</p>
    <div class="abs rule" style="left:118px;top:712px;width:180px;background:#fff"></div>
    <p class="abs offer-copy" style="top:719px">As a way to give back to my community,<br>I am offering new clients</p>
    <div class="abs pill offer-pill">SIX FREE COACHING SESSIONS</div>
    <p class="abs offer-note">*This is a limited time offer.</p>

    <div class="abs contact-band"></div>
    <div class="abs portrait" role="img" aria-label="Portrait photo of Joan Talvery"></div>
    <div class="abs pill contact-pill">PLEASE CONTACT ME</div>
    <div class="abs contact-text">
      <span class="note">I’m ready to support you as you work to improve your health.</span>
      <span class="who">Joan Talvery</span>
      <span class="row"><svg viewBox="0 0 24 24"><path d="M6.6 10.8a15 15 0 0 0 6.6 6.6l2.2-2.2c.3-.3.7-.4 1-.2 1.1.4 2.3.6 3.6.6.6 0 1 .4 1 1V20c0 .6-.4 1-1 1A17 17 0 0 1 3 4c0-.6.4-1 1-1h3.5c.6 0 1 .4 1 1 0 1.3.2 2.5.6 3.6.1.3 0 .7-.2 1z" fill="#fff"/></svg>555-014-2298</span>
      <span class="row"><svg viewBox="0 0 24 24"><rect x="3" y="5" width="18" height="14" fill="none" stroke="#fff" stroke-width="2"/><path d="M3 6l9 7 9-7" fill="none" stroke="#fff" stroke-width="2"/></svg>talveryhwc@example.com</span>
    </div>
  </section>

</div>
</body>
</html>
```